Industry automation wholesale website

www.velqora.eu provides solutions for automation, building automation and digital signage.

Our products are rugged, reliable, energy saving and representative.

Scope of pages:
● welcome page
- scope of products
- applications, success stories and news
● category page
- short introduction
- sub categories
- product highlights
● product page
- short introduction
- about 3 to 4 pictures
- technical specifications: materials, dimensions
- price
- related products

Optional:
● contact page
- address
- contact form
● blog
- picture
- text
● logo
● favicon / apple touch icon

Conclusion:
● We need a professionally looking site
● Bright colors (e.g. white, grey, metalic colors, blue)

some pages we like:
http://www.brundafel.de/
http://www.korvimash.de/

Target Market(s)

Our target market is the industrial sector
● Target audience: engineering and IT professionals

Industry/Entity Type

Building

Requirements
Must have
• ● only use free available fonts e.g. Pellor Type Library (http://www.pellortype.com/webfonts)
Should not have
• ● sound
● flash

```html
<!DOCTYPE html>
<html lang="en">
<head>
<meta charset="utf-8">
<title>Velqora – Product</title>
<link href="https://fonts.googleapis.com/css2?family=Montserrat:ital,wght@0,400;0,600;0,700;1,400&family=Roboto+Slab:wght@400&display=swap" rel="stylesheet">
<style>
:root{
  --blue:#1a95cf;
  --blue-dark:#0d3f8f;
  --blue-deep:#0a2f7a;
  --blue-light:#cde8f5;
  --ink:#2b2b2b;
  --text:#555;
  --muted:#8a8a8a;
  --line:#dcdcdc;
  --white:#fff;
}
*{margin:0;padding:0;box-sizing:border-box}
html,body{width:685px;height:1200px;overflow:hidden;background:var(--white)}
body{position:relative;font-family:'Montserrat',sans-serif;color:var(--text);font-size:6px;line-height:1.5}
.abs{position:absolute}
.top-strip{left:0;top:0;width:685px;height:4px;background:linear-gradient(90deg,var(--blue-dark),var(--blue),var(--blue-dark))}
.account-bar{top:13px;left:473px;display:flex;gap:0;font-size:6px;color:var(--blue)}
.account-bar span{padding:0 8px;border-right:1px solid var(--line)}
.account-bar span:first-child{padding-left:0}
.account-bar span:last-child{border:none}
.brand{left:22px;top:32px;font-size:27px;font-weight:600;color:var(--blue-dark);letter-spacing:-.5px;display:flex;align-items:center;gap:6px}
.brand i{display:block;width:9px;height:9px;border-radius:50%;background:var(--blue)}
.main-nav{top:60px;left:358px;display:flex;gap:0;font-size:5.5px;font-weight:600;color:#444;letter-spacing:.3px}
.main-nav a{color:inherit;text-decoration:none;position:absolute;white-space:nowrap}
.main-nav .active{color:var(--blue)}
.nav-marker{left:395px;top:98px;width:35px;height:3px;background:var(--blue)}
.search-icon{left:646px;top:59px}
.header-rule{left:0;top:101px;width:685px;height:1px;background:var(--line);box-shadow:0 2px 3px rgba(0,0,0,.08)}
.breadcrumb{left:22px;top:106px;font-size:5.5px;color:var(--muted)}
.category-menu{left:22px;top:158px;width:130px;list-style:none;font-size:6px;color:#333}
.category-menu li{border-bottom:1px solid var(--line);height:18.5px;line-height:16px}
.category-menu .sub{border:none;height:auto}
.category-menu .sub div{margin-left:20px;height:13px;line-height:12px;color:var(--blue);font-size:5.8px}
.category-menu .sub .current{background:var(--blue);color:var(--white);margin-left:18px;padding-left:2px;font-weight:600}
.category-menu .sub{border-bottom:1px solid var(--line);padding-bottom:5px}
.product-visual{left:197px;top:155px;width:132px;height:123px;background:linear-gradient(160deg,#3b3b3b 0%,#1c1c1c 100%);border-radius:3px}
.product-visual .screen{position:absolute;left:9px;top:8px;width:114px;height:97px;background:linear-gradient(135deg,#bcd9ee,#6ea5cc)}
.gallery-dots{left:197px;top:291px;display:flex;gap:2px}
.gallery-dots i{width:6px;height:6px;border-radius:50%;background:#999;display:block}
.gallery-dots i:first-child{background:var(--blue)}
.zoom{left:297px;top:290px;font-size:6px;color:#444;display:flex;gap:3px;align-items:center}
.product-info{left:369px;top:155px;width:275px}
.product-title{font-size:11.5px;font-weight:400;color:var(--ink);letter-spacing:.3px;margin-bottom:11px}
.spec-label{font-size:5.5px;font-weight:700;color:var(--blue);letter-spacing:.2px;margin-top:9px}
.spec-text{font-size:5.8px;color:#444;line-height:1.85}
.price{font-size:11px;font-weight:700;color:#333;line-height:1.2}
.price-note{font-size:4.8px;color:#444;line-height:1.35}
.price-note b{color:var(--blue)}
.cart-row{left:369px;top:362px;display:flex;align-items:center;font-size:5px;color:var(--muted)}
.qty{width:38px;height:13px;background:#d4d4d4;margin-left:6px}
.add-cart{margin-left:4px;width:113px;height:13px;background:var(--blue);color:var(--white);font-size:5px;font-weight:600;text-align:center;line-height:13px}
.section-title{font-family:'Roboto Slab',serif;font-size:9px;color:#333;letter-spacing:.3px}
.related-title{left:0;width:685px;top:418px;text-align:center}
.related-rule{left:0;top:438px;width:685px;height:1px;background:var(--line)}
.slider-arrow{top:495px;width:24px;height:24px;background:var(--blue-light);color:var(--blue-dark);font-size:10px;text-align:center;line-height:24px}
.related-divider{left:324px;top:456px;width:1px;height:100px;background:var(--line)}
.related-card h3{font-size:10.5px;font-weight:400;color:var(--blue-dark);line-height:1.3;width:140px}
.related-card p{font-size:5.8px;color:#444;margin-top:8px;width:135px;line-height:1.75}
.read-more{font-size:4.8px;font-weight:700;color:var(--blue);letter-spacing:.2px}
.thumb{border-radius:2px}
.cta-band{left:0;top:577px;width:685px;height:92px;background:linear-gradient(100deg,#3aa4dc 0%,#1d64b8 45%,var(--blue-deep) 100%);color:var(--white);font-size:13px;font-weight:400;text-align:center;line-height:92px;letter-spacing:.2px}
.news-title{left:55px;top:720px;font-size:13px;color:#444}
.testimony-title{left:476px;width:160px;top:720px;font-size:13px;color:#444;text-align:center}
.news-list{left:55px;top:747px;width:360px}
.news-item{margin-bottom:17px}
.news-date{font-size:5.5px;font-weight:700;color:var(--blue)}
.news-item p{font-size:6px;color:#777;line-height:1.75}
.news-item p strong{font-size:8.8px;color:var(--blue);font-weight:600}
.news-item p em{font-style:normal;color:var(--blue)}
.news-sep{width:80px;height:1px;background:var(--line);margin-top:8px}
.column-divider{left:450px;top:740px;width:1px;height:220px;background:var(--line)}
.testimony-photo{left:476px;top:752px;width:161px;height:105px;background:linear-gradient(120deg,#dfe7ee 0%,#aebfce 45%,#4d5c6e 100%)}
.testimony-name{left:476px;width:161px;top:880px;font-size:5.5px;font-weight:700;color:#333;text-align:center}
.testimony-quote{left:476px;width:161px;top:889px;font-size:6px;font-style:italic;color:var(--blue);text-align:center;line-height:1.6}
.footer{left:0;top:1004px;width:685px;height:168px;background:linear-gradient(110deg,var(--blue-deep) 0%,#1c5fb4 55%,#4fb0e6 100%);color:var(--white)}
.footer h4{position:absolute;top:27px;font-size:6px;font-weight:700;letter-spacing:.3px}
.footer ul{position:absolute;top:48px;list-style:none;font-size:5.5px;line-height:1.45}
.footer .address{position:absolute;top:48px;left:212px;font-size:5.3px;font-weight:600;line-height:1.45}
.newsletter-lead{position:absolute;left:475px;top:44px;font-size:5.5px;font-weight:600}
.newsletter-input{position:absolute;left:475px;top:59px;width:164px;height:17px;background:var(--white);color:#999;font-size:5px;font-style:italic;line-height:17px;padding-left:5px}
.newsletter-go{position:absolute;left:641px;top:59px;width:20px;height:17px;background:var(--blue-deep);font-size:5.5px;text-align:center;line-height:17px}
.copyright{left:55px;top:1184px;font-size:4.5px;color:#555;letter-spacing:.2px}
</style>
</head>
<body>
<div class="abs top-strip"></div>

<div class="abs account-bar">
  <span>Sign Out</span><span>My Account &#9662;</span><span>English &#9662;</span><span>&#128722; 0€</span>
</div>

<div class="abs brand">velqora<i></i></div>

<nav class="abs main-nav">
  <a style="left:0">HOME</a>
  <a class="active" style="left:38px">PRODUCTS</a>
  <a style="left:89px">APPLICATIONS</a>
  <a style="left:150px">SUPPORT</a>
  <a style="left:195px">ABOUT US</a>
  <a style="left:241px">CONTACT</a>
</nav>
<svg class="abs search-icon" width="9" height="9" viewBox="0 0 10 10"><circle cx="4" cy="4" r="3" fill="none" stroke="#444" stroke-width="1.2"/><line x1="6.2" y1="6.2" x2="9" y2="9" stroke="#444" stroke-width="1.3"/></svg>
<div class="abs nav-marker"></div>
<div class="abs header-rule"></div>

<div class="abs breadcrumb">Products › Touch Panel Computer › 3 Category</div>

<ul class="abs category-menu">
  <li>Automation Technology</li>
  <li style="border:none;height:13px;line-height:13px">Touch Panel Computer</li>
  <li class="sub">
    <div>1 category</div>
    <div>2 category</div>
    <div class="current">3 category</div>
  </li>
  <li>Fieldbus DAQ</li>
  <li>Industry PC</li>
  <li>Remote IO</li>
  <li>Embedded Systems</li>
  <li>Modbus RTU</li>
  <li>Human Machine Interface</li>
  <li>RS485 Converter</li>
  <li>RS422 Repeater</li>
</ul>

<div class="abs product-visual" role="img" aria-label="Touch panel monitor with a finger tapping an on-screen keyboard"><div class="screen"></div></div>
<div class="abs gallery-dots"><i></i><i></i><i></i></div>
<div class="abs zoom">Zoom <svg width="7" height="7" viewBox="0 0 10 10"><circle cx="4" cy="4" r="3" fill="none" stroke="#444" stroke-width="1.3"/><line x1="6.2" y1="6.2" x2="9" y2="9" stroke="#444" stroke-width="1.4"/></svg></div>

<section class="abs product-info">
  <h1 class="product-title">PRODUCT NAME</h1>
  <div class="spec-label">FEATURES</div>
  <p class="spec-text">&nbsp;Mei ex legere civibus phaedrum. Id eam putent conceptam. Ad malis nihil epicurei dolorum torquatos ut, prolegere ipsum.Mei ex legere civibus phaedrum. Id eam putent</p>
  <div class="spec-label">TECHNICAL INFORMATION</div>
  <p class="spec-text">Ad malis nihil epicurei dolorum torquatos ut, prolegere ipsum.Mei ex legere civibus phaedrum. Id eam putent conceptam. Ad malis nihil epicurei dolorum torquatos ut, prolegere ipsum.</p>
  <div class="spec-label">MEASUREMENTS</div>
  <p class="spec-text">&nbsp;0000 x 0000 x 0000</p>
  <div class="spec-label">PRICE</div>
  <div class="price">0000€</div>
  <p class="price-note">Incl. 19% VAT: 95,20 €<br>shipping to Germany: 8,00 €<br><b>shipping inside EU</b></p>
</section>

<div class="abs cart-row">Quant <div class="qty"></div><div class="add-cart">Add to Shopping Cart</div></div>

<h2 class="abs section-title related-title">RELATED PRODUCTS</h2>
<div class="abs related-rule"></div>
<div class="abs slider-arrow" style="left:0">&#8249;</div>
<div class="abs slider-arrow" style="left:660px">&#8250;</div>

<div class="abs thumb" style="left:80px;top:465px;width:65px;height:80px;background:linear-gradient(180deg,#9aa3ab,#4f565c)" role="img" aria-label="Two pedestal mounted touch terminals"></div>
<article class="abs related-card" style="left:160px;top:462px">
  <h3>Eum ex, laoreet iudicabit posid onium quo te.</h3>
  <p>Mei ex legere civibus phaedrum. Id eam putent conceptam. Ad malis nihil epicurei dolorum torquatos ut, prolegere ipsum.</p>
  <div class="read-more" style="margin-top:10px">READ MORE HERE</div>
</article>
<div class="abs related-divider"></div>
<div class="abs thumb" style="left:355px;top:465px;width:75px;height:75px;background:linear-gradient(135deg,#c7b8e8,#6a2fb8 55%,#2a1460)" role="img" aria-label="Widescreen display panel with a purple screen"></div>
<article class="abs related-card" style="left:453px;top:462px">
  <h3>Eum ex, laoreet iudicabit posid onium quo te.</h3>
  <p>Mei ex legere civibus phaedrum. Id eam putent conceptam. Ad malis nihil epicurei dolorum torquatos ut, prolegere ipsum.</p>
  <div class="read-more" style="margin-top:10px">READ MORE HERE</div>
</article>

<div class="abs cta-band">Have a question? Call us at +49 211 540 27 83 or info@velqora.de</div>

<h2 class="abs section-title news-title">NEWS</h2>
<h2 class="abs section-title testimony-title">TESTEMONY</h2>

<section class="abs news-list">
  <div class="news-item">
    <div class="news-date">Jan/05</div>
    <p><strong>Eum ex, laoreet iudicabit posid onium quo te.</strong> Mei ex legere civibus phaedrum. Id eam putent conceptam. Ad malis nihil epicurei dolorum torquatos ut, cu prolegere civibus phaedrum. Id eam putent conceptam movet debitis graecis.Eum ex, laoreet iudicabit posid onium quo te Id eam putent conceptam movet debitis Ad malis nihil epicurei dolorum torquatos ut, cu prolegere civibus phaedrum. <em>(...)</em></p>
    <div class="news-sep"></div>
  </div>
  <div class="news-item">
    <div class="news-date">Dec/15</div>
    <p><strong>Eum ex, laoreet iudicabit posid onium quo te.</strong> Eum ex, laoreet iudicabit posid onium quo te. Mei ex legere civibus phaedrum. Id eam putent conceptam. Ad malis nihil epicurei dolorum torquatos ut, cu prolegere civibus phaedrum. Id eam putent conceptam movet debitis Ad malis nihil epicurei torquatos ut, cu prolegere. <em>(...)</em></p>
    <div class="news-sep"></div>
  </div>
  <div class="news-item">
    <div class="news-date">Dec/07</div>
    <p><strong>Eum ex, laoreet iudicabit posid onium quo te.</strong> Mei ex legere civibus phaedrum. Id eam putent conceptam. Ad malis nihil epicurei dolorum torquatos ut, cu prolegere civibus phaedrum. Id eam putent conceptam movet debitis graecis.Eum ex, laoreet iudicabit posid onium quo te Id eam putent conceptam movet debitis Ad malis nihil epicurei dolorum torquatos ut, cu prolegere civibus phaedrum. <em>(...)</em></p>
  </div>
  <div class="read-more">READ MORE HERE</div>
</section>

<div class="abs column-divider"></div>
<div class="abs testimony-photo" role="img" aria-label="Business executive in an office with colleagues in the background"></div>
<div class="abs testimony-name">Mark Halden, CEO of TORVEX</div>
<p class="abs testimony-quote">"Mei ex legere civibus phaedrum. Id eam putent conceptam. Ad malis nihil epicurei dolorum torqua-tos ut, cu prolegere civibus etphaedrum. Id eam putent conceptam movet debitis vix et."(...)</p>
<div class="abs read-more" style="left:476px;width:161px;top:946px;text-align:center">READ MORE HERE</div>

<footer class="abs footer">
  <h4 style="left:55px">MAIN MENU</h4>
  <ul style="left:55px"><li>Home</li><li>Products</li><li>Applications</li><li>Support</li><li>About Us</li><li>Contact</li></ul>
  <h4 style="left:125px">OTHER OPTIONS</h4>
  <ul style="left:125px"><li>News</li><li>Testemony</li><li>Privacy &amp; Legal</li><li>FAQ's</li><li>Help</li><li>Site Map</li></ul>
  <h4 style="left:212px">CONTACT</h4>
  <div class="address">Velqora Brenner<br>Lindenallee 14<br>40225 Düsseldorf<br><br>Phone: +49 211 540 27 83<br>Telefax: +49 211 540 27 84<br>Email: info@velqora.eu</div>
  <h4 style="left:475px">NEWSLETTER</h4>
  <div class="newsletter-lead">Sign up now to receive our regular emails</div>
  <div class="newsletter-input">Enter your mail address</div>
  <div class="newsletter-go">Go</div>
</footer>

<div class="abs copyright">VELQORA - ANALOG DIGITAL MEASUREMENTS &nbsp;|&nbsp; ALL RIGHTS RESERVED @ 2014</div>
</body>
</html>
```